依頼詳細
箱の正面部分のみのデザインの依頼になります。
海外向けの商品のため英語表示のみでお願いします。
アジア向けの商品になりますのであまりスタイリッシュ過ぎずかわいらしいデザインを希望します
記載項目
商品名「MOCHI DREAM`S」
ブランド名「Tilko」
味 「Tuna&Salmon Flavor」
特徴「Hairball Control」(natural fiber helps reduce hairball formation)
内容量400g
サイズ W 12・H18
希望イメージ
シンプル 複雑
単色 カラフル
暗い 明るい
日常 高級
遊び心 厳粛
未来的 伝統的
女性的 男性的
希望する色
納品ファイル
• 高解像度JPG (.jpg)
• イラストレーター形式 (.ai)
補足説明
ブランドロゴ(添付)はあまり前面に出ないデザインを希望します。
■ 選んだ理由

シンプルと可愛らしさ、商品になった時のイメージが希望のものでした。
細かい修正依頼にもきちんと対応して下さり、満足行くデザインに仕上がりました。

■ 提案者全員のお礼・コメント

たくさんの提案を頂きありがとうございました。
どのデザインも本当に素敵でとても迷い、全てのデザインで商品サンプルを作りました。
現地人やペット業界の方々に好きな物を選んで頂いたのですが、意見がかなり分かれてどのデザインに決めるかを苦労しました。
今回はお一人しか採用出来ませんでしたが、またお願いしたいと思っております。
その時はどうぞよろしくお願いします。
ありがとうございました。

```html
<!DOCTYPE html>
<html lang="en">
<head>
<meta charset="utf-8">
<title>MOCHI DREAM`S – Hairball Control</title>
<link rel="stylesheet" href="https://fonts.googleapis.com/css2?family=Fredoka:wght@500;600;700&display=swap">
<style>
  :root{
    --bg-top:#7a2a9c;
    --bg-mid:#c42a8a;
    --bg-bottom:#e8305a;
    --swoosh-white:#fff7f0;
    --swoosh-gold:#e8b04a;
    --ribbon-blue:#2f8fe0;
    --ribbon-dark:#1a5fae;
    --title-yellow:#ffd43a;
    --title-orange:#f07d18;
    --title-shadow:#6b2a12;
    --text-white:#ffffff;
    --flavor-pink:#e77bb6;
    --flavor-text:#5a2356;
    --cat-grey:#8c8f9e;
    --cat-light:#e9e9ef;
    --kibble-red:#c2263a;
    --kibble-green:#93a23a;
    --kibble-yellow:#e5b73f;
  }
  *{margin:0;padding:0;box-sizing:border-box}
  html,body{width:800px;height:1200px;overflow:hidden}
  body{font-family:"Fredoka",sans-serif}
  .package-front{
    position:relative;width:800px;height:1200px;overflow:hidden;
    background:linear-gradient(180deg,var(--bg-top) 0%,var(--bg-mid) 35%,var(--bg-bottom) 70%,var(--bg-bottom) 100%);
  }
  .brand{
    position:absolute;z-index:3;top:18px;left:0;width:100%;
    display:flex;flex-direction:column;align-items:center;gap:2px;
    color:var(--text-white);font-weight:500;font-size:32px;letter-spacing:1px;line-height:1.1;
  }
  .brand-dot{width:20px;height:20px;border-radius:50%;border:3px solid var(--text-white)}
  .swoosh{position:absolute;left:0;top:170px;width:800px;height:560px}
  .cat-illustration{
    position:absolute;left:200px;top:110px;width:420px;height:360px;
    border-radius:48% 48% 30% 30%;
    background:radial-gradient(ellipse at 50% 45%,var(--cat-light) 0%,#c9cad6 40%,var(--cat-grey) 100%);
  }
  .ribbon{position:absolute;left:20px;top:350px;width:760px;height:270px}
  .product-name{
    position:absolute;z-index:2;top:392px;left:0;width:100%;text-align:center;
    font-family:"Fredoka",sans-serif;font-weight:700;color:var(--title-yellow);
    -webkit-text-stroke:8px var(--title-orange);paint-order:stroke fill;
    text-shadow:0 6px 0 var(--title-shadow),0 8px 10px rgba(0,0,0,.35);
    line-height:.9;
  }
  .product-name .line-one{display:block;font-size:108px;letter-spacing:4px}
  .product-name .line-two{display:block;font-size:100px;letter-spacing:3px}
  .feature{
    position:absolute;z-index:2;top:596px;left:0;width:100%;text-align:center;
    font-weight:700;font-size:40px;letter-spacing:1.5px;
    color:var(--title-yellow);-webkit-text-stroke:5px var(--title-shadow);paint-order:stroke fill;
  }
  .feature-note{
    position:absolute;z-index:2;top:648px;left:0;width:100%;text-align:center;
    font-weight:700;font-size:24px;color:var(--text-white);
    text-shadow:0 2px 3px rgba(0,0,0,.45);
  }
  .kibble-photo{
    position:absolute;left:0;top:680px;width:800px;height:520px;
    background:
      radial-gradient(circle at 20% 30%,var(--kibble-yellow) 0 6%,transparent 14%),
      radial-gradient(circle at 70% 25%,var(--kibble-green) 0 7%,transparent 16%),
      radial-gradient(circle at 45% 60%,var(--kibble-yellow) 0 5%,transparent 13%),
      radial-gradient(circle at 85% 70%,var(--kibble-green) 0 6%,transparent 14%),
      radial-gradient(circle at 10% 80%,var(--kibble-green) 0 6%,transparent 14%),
      linear-gradient(180deg,rgba(232,48,90,0) 0%,var(--kibble-red) 12%,#a11f35 100%);
  }
  .flavor-label{
    position:absolute;left:225px;top:958px;width:300px;height:52px;
    background:var(--flavor-pink);opacity:.95;
    display:flex;align-items:center;justify-content:center;
    font-weight:600;font-size:25px;color:var(--flavor-text);
  }
  .net-weight{
    position:absolute;left:612px;top:915px;width:178px;height:178px;border-radius:50%;
    background:var(--text-white);color:var(--flavor-text);
    display:flex;flex-direction:column;align-items:center;justify-content:center;
    font-weight:700;line-height:1;
  }
  .net-weight .amount{font-size:50px}
  .net-weight .unit{font-size:30px;margin-top:6px}
</style>
</head>
<body>
<main class="package-front">
  <svg class="swoosh" viewBox="0 0 800 560" aria-hidden="true">
    <path d="M-20 330 C 120 80, 420 -20, 820 120 L 820 190 C 470 60, 190 140, 40 370 Z" fill="var(--swoosh-gold)"/>
    <path d="M-20 320 C 130 90, 420 0, 820 130 L 820 170 C 460 50, 180 130, 20 350 Z" fill="var(--swoosh-white)"/>
  </svg>

  <div class="cat-illustration" role="img" aria-label="Illustration of a grey and white cartoon cat"></div>

  <div class="brand"><span class="brand-dot"></span><span class="brand-name">Tilko</span></div>

  <svg class="ribbon" viewBox="0 0 760 270" aria-hidden="true">
    <path d="M0 170 L70 150 L50 205 L80 250 L10 250 Z" fill="var(--ribbon-dark)"/>
    <path d="M760 170 L690 150 L710 205 L680 250 L750 250 Z" fill="var(--ribbon-dark)"/>
    <path d="M55 140 Q380 90 705 140 L705 235 Q380 190 55 235 Z" fill="var(--ribbon-blue)"/>
  </svg>

  <h1 class="product-name"><span class="line-one">MOCHI</span><span class="line-two">DREAM`S</span></h1>
  <p class="feature">Hairball Control</p>
  <p class="feature-note">natural fiber helps reduce hairball formation</p>

  <div class="kibble-photo" role="img" aria-label="Photo of colourful red, green and yellow dry cat food kibble"></div>

  <div class="flavor-label">Tuna&amp;Salmon Flavor</div>
  <div class="net-weight"><span class="amount">400g</span><span class="unit">NET</span></div>
</main>
</body>
</html>
```